Technology Company Web Design Project

We are working with BrimLoop. They are a technology company and in need of a new website design.
BrimLoop helps companies control who (or what) can access which information inside their systems — and under what conditions. Think of them as the traffic controller for digital access and data permissions.
Instead of letting every app, employee, or AI bot freely connect to everything, GateMarrow makes sure:
• Each one only gets access to what it actually needs.
• That access follows company rules automatically.
• Those rules are enforced the same way everywhere — across apps, servers, and even AI tools.
Some competitor sites to use for inspiration:
https://www.korvanshield.com/en/lp/ac/korvanmesh.html
https://www.dunmerecharter.org
https://www.qelvo.com
Thank you for taking the time to consider designing a website for us. We are web developers based in Stockton and Los Angeles, CA, USA. Most of our projects go through the same process. Understanding this process may help you win a project with us. We custom-code all of our websites in-house. We don’t have any requirements as to what tools you use for your design, but we prefer Figma files. For any design that we label as four-stars, we send it to the client for review. The client picks the final design they want us to use. Once we complete this process, we will continue to show additional clients all the four-star sites and purchase them later. Your designs will have multiple chances to sell. For better chances of success, we ask that you follow these guidelines.
IMAGES:
If you use any images or icons in the design, we ask that you have a link to the asset so we can purchase the image/icon. Most of the designs we submit do not have the customer’s images on them unless they have some great images. Be creative; show us the feeling you are trying to portray with your image choices. Use any royalty-free site you choose. We subscribe to Tarsel and mainly use their images, but we can purchase images outside of Tarsel.
PLEASE NOTE: we will not submit designs to clients with watermarks on the images.
FONTS:
We ask that you identify the fonts used in the design. This can be done in a message if you want. We typically use Google Fonts and Tarsel Fonts.
CONTENT:
We're always open to different content and ideas. We often submit designs with stock images so the client can see our vision. We typically take pictures after the website launch to use their images with our vision. Lorem Ipsum is fine for paragraphs, but we ask that you write the headers in correct English. We want to be able to show the vision and identify the sections of the website.
INSPIRATION:
We typically add a couple of links in the brief of websites we like to help you get started in your design.
REVISIONS:
We do not often ask for revisions of the designs unless we see something in the design that may not appeal to the client. If there are slight changes that we want to make, we do that in the development process.
FEEDBACK:
We rarely give feedback on designs during the design process. We are working on many website projects and do not have the time to provide feedback. We usually respond if your request is well thought out and asks specific questions, but a note asking “feedback, please” usually goes unanswered.

```html
<!DOCTYPE html>
<html lang="en">
<head>
<meta charset="utf-8">
<title>BrimLoop — Digital Access Control</title>
<link href="https://fonts.googleapis.com/css2?family=Poppins:wght@300;400;500;600&display=swap" rel="stylesheet">
<style>
:root{
  --navy:#1f3a5f;
  --orange:#ee7d22;
  --ink:#333d4a;
  --muted:#5a6270;
  --line:#d9dde3;
  --hero-bg:#efefef;
  --footer:#223a5e;
  --white:#fff;
}
*{box-sizing:border-box;margin:0;padding:0}
html,body{width:1200px;height:4332px;overflow:hidden}
body{font-family:'Poppins',sans-serif;color:var(--ink);background:var(--white);position:relative}
.abs{position:absolute}
.btn{position:absolute;background:var(--orange);color:var(--white);border-radius:24px;font-size:14px;display:flex;align-items:center;justify-content:center;font-weight:400;letter-spacing:.3px}
.brand{display:flex;align-items:center;gap:10px;font-weight:600;color:var(--orange);letter-spacing:1px}
.brand .mark{width:26px;height:26px;border-radius:50%;background:var(--navy)}
/* header */
.nav{position:absolute;top:76px;left:555px;display:flex;gap:0;font-size:13px;color:var(--ink)}
.nav span{position:absolute;white-space:nowrap}
.nav .active{color:var(--orange)}
/* section headings */
.sec-title{position:absolute;left:0;width:1200px;text-align:center;font-size:47px;font-weight:500;color:var(--navy);letter-spacing:.5px}
.sec-title em,.h-split em{font-style:normal;color:var(--orange)}
.bar{position:absolute;height:4px;width:60px;background:var(--navy)}
.para{position:absolute;font-size:13.5px;line-height:25px;color:var(--ink)}
.photo{position:absolute}
/* cards */
.feature{position:absolute;top:775px;height:190px;background:var(--white);box-shadow:0 3px 10px rgba(0,0,0,.18);display:flex;flex-direction:column;align-items:center;justify-content:center;text-align:center;font-size:24px;line-height:29px;color:#222;font-weight:400}
.feature svg{margin-bottom:10px}
.sol{position:absolute;top:1790px;width:225px}
.sol .ic{width:70px;height:70px;border-radius:50%;display:flex;align-items:center;justify-content:center}
.sol h3{font-size:17px;font-weight:500;margin-top:32px;letter-spacing:.2px}
.sol p{font-size:13px;line-height:21.5px;margin-top:18px;text-align:justify;color:var(--ink)}
.sol .go{margin-top:14px;width:20px;height:20px;transform:rotate(45deg);margin-left:4px}
.divider{position:absolute;top:1790px;width:3px;height:355px;background:var(--line)}
.res{position:absolute;top:3085px;width:292px;height:375px;background:var(--white);box-shadow:0 3px 10px rgba(0,0,0,.18);overflow:hidden}
.res .img{position:absolute;left:8px;top:6px;width:282px;height:192px}
.res h4{position:absolute;left:22px;top:230px;font-size:16px;font-weight:500;color:var(--navy)}
.res .u{position:absolute;left:22px;top:262px;width:46px;height:2px;background:var(--navy)}
.res p{position:absolute;left:22px;top:280px;width:230px;font-size:14px;line-height:20px;text-align:justify;color:var(--ink)}
.res .corner{position:absolute;right:0;bottom:0;width:0;height:0;border-left:54px solid transparent;border-bottom:54px solid var(--orange)}
.res .corner-arrow{position:absolute;right:8px;bottom:6px}
.arrow-btn{position:absolute;top:3270px;width:44px;height:44px;border-radius:50%;border:2px solid #c7ccd3;background:var(--white);display:flex;align-items:center;justify-content:center}
.partner{position:absolute;top:3762px;height:166px;background:var(--white);box-shadow:0 2px 10px rgba(0,0,0,.15);display:flex;align-items:center;justify-content:center;gap:8px;font-size:18px;font-weight:500;color:#111}
.partner .dot{width:22px;height:22px;border-radius:50%;background:#111}
/* footer */
.footer{position:absolute;top:3990px;left:0;width:1200px;height:290px;background:var(--footer);color:var(--white)}
.footer h5{position:absolute;font-size:16px;font-weight:400;letter-spacing:.3px}
.qlinks{position:absolute;left:305px;top:100px;font-size:13px;line-height:27px;list-style:none}
.qlinks li::before{content:"";display:inline-block;width:18px;height:2px;background:var(--white);margin-right:8px;vertical-align:middle;opacity:.8}
.contact-row{position:absolute;left:770px;display:flex;gap:20px;font-size:13px;line-height:15px}
.contact-row .box{width:26px;height:26px;border:1.5px solid var(--white);border-radius:4px;display:flex;align-items:center;justify-content:center;flex:none;margin-top:2px}
.social{position:absolute;top:4195px;width:28px;height:28px;border:1.5px solid var(--white);border-radius:50%}
.copy{position:absolute;top:4280px;left:0;width:1200px;height:52px;background:var(--orange);color:var(--white);font-size:12px;display:flex;align-items:center;justify-content:center}
</style>
</head>
<body>

<!-- header -->
<div class="abs brand" style="left:70px;top:42px;font-size:30px;color:var(--orange)"><span class="mark"></span>BrimLoop</div>
<svg class="abs" style="left:1026px;top:18px" width="110" height="22" viewBox="0 0 110 22" fill="none" stroke="#1f3a5f" stroke-width="1.8">
  <circle cx="10" cy="10" r="7"/><line x1="15" y1="15" x2="20" y2="20"/>
  <circle cx="54" cy="11" r="9"/><circle cx="54" cy="8" r="3"/><path d="M48 17c2-3 10-3 12 0"/>
  <circle cx="95" cy="11" r="9"/><ellipse cx="95" cy="11" rx="4" ry="9"/><line x1="86" y1="11" x2="104" y2="11"/>
</svg>
<div class="nav">
  <span class="active" style="left:0">HOME</span>
  <span style="left:75px">ABOUT</span>
  <span style="left:150px">PRODUCT</span>
  <span style="left:248px">SOLUTION</span>
  <span style="left:347px">RESOURCES</span>
</div>
<div class="btn" style="left:1015px;top:70px;width:118px;height:28px;font-size:12px">CONTACT US</div>

<!-- hero -->
<div class="abs" style="left:0;top:142px;width:1200px;height:568px;background:linear-gradient(90deg,#f2f2f2 0%,#ebebeb 45%,#e6e6e6 100%)"></div>
<div class="photo" role="img" aria-label="Server racks with a glowing circuit padlock representing secure data access" style="left:510px;top:142px;width:690px;height:560px;background:radial-gradient(ellipse at 52% 50%,#4fd3e6 0%,#1c6f8a 30%,#122838 62%,rgba(230,230,230,0) 85%)"></div>
<div class="abs" style="left:65px;top:223px;font-size:21px;color:#222">Welcome to</div>
<div class="abs" style="left:62px;top:250px;font-size:80px;font-weight:600;color:var(--navy);letter-spacing:2px">BRIM <span style="color:var(--orange)">LOOP</span></div>
<div class="abs" style="left:65px;top:372px;font-size:20px;line-height:35px;color:#222">THE TRAFFIC CONTROLLER FOR DIGITAL<br>ACCESS AND DATA PERMISSIONS</div>
<div class="btn" style="left:60px;top:456px;width:137px;height:44px">CONTACT US</div>

<!-- features -->
<div class="feature" style="left:92px;width:303px">
  <svg width="76" height="72" viewBox="0 0 76 72" fill="none" stroke="#1f3a5f" stroke-width="2.5"><rect x="8" y="4" width="40" height="56" rx="3"/><line x1="16" y1="18" x2="40" y2="18"/><line x1="16" y1="28" x2="40" y2="28"/><line x1="16" y1="38" x2="32" y2="38"/><rect x="40" y="40" width="26" height="22" rx="3" stroke="#ee7d22"/><path d="M45 40v-6a8 8 0 0 1 16 0v6" stroke="#ee7d22"/><circle cx="53" cy="51" r="3" stroke="#ee7d22"/></svg>
  Data Privacy
</div>
<div class="feature" style="left:445px;width:305px">
  <svg width="80" height="76" viewBox="0 0 80 76" fill="none" stroke="#ee7d22" stroke-width="2.2"><circle cx="20" cy="10" r="4"/><circle cx="8" cy="30" r="4"/><circle cx="36" cy="8" r="4"/><path d="M22 14l10 14M12 30h18M36 12v14"/><path d="M38 72l-10-18c-2-4 3-7 6-4l6 8V30c0-4 6-4 6 0v14l4-1c3 0 4 2 4 2l4-1c3 0 4 3 4 3l4 0c4 0 5 3 5 6v6l-4 13z" stroke="#1f3a5f"/></svg>
  Trustworthy<br>Interactions
</div>
<div class="feature" style="left:804px;width:304px">
  <svg width="72" height="72" viewBox="0 0 72 72" fill="none" stroke="#1f3a5f" stroke-width="2.4"><path d="M36 4l6 8 10-2 2 10 9 5-4 9 4 9-9 5-2 10-10-2-6 8-6-8-10 2-2-10-9-5 4-9-4-9 9-5 2-10 10 2z"/><circle cx="36" cy="36" r="14" stroke="#ee7d22"/><path d="M29 36l5 5 9-10" stroke="#ee7d22"/></svg>
  Precision &amp;<br>Compliance
</div>

<!-- about -->
<div class="photo" role="img" aria-label="Hands typing on a laptop with floating security and identity icons" style="left:80px;top:1095px;width:534px;height:355px;background:linear-gradient(135deg,#c8cfd6 0%,#e8eaec 40%,#9aa7b2 75%,#5d6b77 100%)"></div>
<div class="abs" style="left:88px;top:1103px;width:518px;height:339px;border:1.5px solid var(--orange)"></div>
<div class="abs h-split" style="left:713px;top:1105px;font-size:46px;font-weight:500;color:var(--navy)">ABOUT <em>US</em></div>
<div class="bar" style="left:715px;top:1172px"></div>
<p class="para" style="left:713px;top:1220px;width:420px">Lorem ipsum dolor sit amet, consectetur adipiscing elit, sed do eiusmod tempor incididunt ut labore et dolore magna aliqua. Quis ipsum suspendisse ultrices gravida. Risus commodo viverra maecenas accumsan lacus vel facilisis. Lorem ipsum dolor sit amet, consectetur adipiscing elit, sed do eiusmod tempor incididunt ut labore et dolore magna aliqua.</p>
<div class="btn" style="left:710px;top:1402px;width:166px;height:43px">KNOW MORE</div>

<!-- solutions -->
<div class="sec-title" style="top:1643px">EXPLORE <em>SOLUTIONS</em></div>
<div class="bar" style="left:570px;top:1711px"></div>

<div class="divider" style="left:335px"></div>
<div class="divider" style="left:602px"></div>
<div class="divider" style="left:866px"></div>

<div class="sol" style="left:92px">
  <div class="ic" style="background:var(--navy)"><svg width="40" height="34" viewBox="0 0 40 34" fill="none" stroke="#fff" stroke-width="1.8"><circle cx="14" cy="10" r="5"/><path d="M4 28c0-7 5-11 10-11s10 4 10 11"/><circle cx="27" cy="17" r="6"/><line x1="31" y1="22" x2="36" y2="27"/></svg></div>
  <h3 style="color:var(--navy)">CUSTOMER IDENTITY</h3>
  <p>Lorem ipsum dolor sit amet, consectetur adipiscing elit, sed do eiusmod tempor incididunt ut labore et dolore magna aliqua.</p>
  <div class="go" style="background:var(--navy)"></div>
</div>
<div class="sol" style="left:370px">
  <div class="ic" style="background:var(--orange)"><svg width="42" height="34" viewBox="0 0 42 34" fill="none" stroke="#fff" stroke-width="1.8"><circle cx="21" cy="9" r="5"/><circle cx="9" cy="13" r="4"/><circle cx="33" cy="13" r="4"/><path d="M11 30c0-7 4-11 10-11s10 4 10 11M2 28c0-5 3-8 7-8M40 28c0-5-3-8-7-8"/></svg></div>
  <h3 style="color:var(--navy)">WORKFORCE IDENTITY</h3>
  <p>Lorem ipsum dolor sit amet, consectetur adipiscing elit, sed do eiusmod tempor incididunt ut labore et dolore magna aliqua.</p>
  <div class="go" style="background:var(--orange)"></div>
</div>
<div class="sol" style="left:633px">
  <div class="ic" style="background:var(--navy)"><svg width="38" height="36" viewBox="0 0 38 36" fill="none" stroke="#fff" stroke-width="1.8"><rect x="3" y="3" width="14" height="12" rx="2"/><rect x="21" y="21" width="14" height="12" rx="2"/><rect x="14" y="12" width="12" height="12" rx="2"/></svg></div>
  <h3 style="color:var(--navy)">B2B IDENTITY</h3>
  <p>Lorem ipsum dolor sit amet, consectetur adipiscing elit, sed do eiusmod tempor incididunt ut labore et dolore magna aliqua.</p>
  <div class="go" style="background:var(--navy)"></div>
</div>
<div class="sol" style="left:903px">
  <div class="ic" style="background:var(--orange)"><svg width="40" height="40" viewBox="0 0 40 40" fill="none" stroke="#fff" stroke-width="1.8"><rect x="9" y="9" width="22" height="22" rx="3"/><text x="20" y="25" font-family="Poppins,sans-serif" font-size="11" fill="#fff" stroke="none" text-anchor="middle">AI</text><path d="M14 9V3M20 9V3M26 9V3M14 37v-6M20 37v-6M26 37v-6M9 14H3M9 20H3M9 26H3M37 14h-6M37 20h-6M37 26h-6"/></svg></div>
  <h3 style="color:var(--navy)">AGENTIC &amp; AI IDENTITY</h3>
  <p>Lorem ipsum dolor sit amet, consectetur adipiscing elit, sed do eiusmod tempor incididunt ut labore et dolore magna aliqua.</p>
  <div class="go" style="background:var(--orange)"></div>
</div>

<div class="btn" style="left:498px;top:2215px;width:204px;height:44px">VIEW ALL&nbsp; SOLUTIONS</div>

<!-- platform -->
<div class="abs h-split" style="left:65px;top:2395px;font-size:46px;line-height:57px;font-weight:500;color:var(--navy)">ONE PLATFORM FOR<br><em>ALL YOUR NEEDS</em></div>
<div class="bar" style="left:67px;top:2528px"></div>
<p class="para" style="left:68px;top:2557px;width:430px">Lorem ipsum dolor sit amet, consectetur adipiscing elit, sed do eiusmod tempor incididunt ut labore et dolore magna aliqua. Quis ipsum suspendisse ultrices gravida. Risus commodo viverra maecenas accumsan lacus vel facilisis. Lorem ipsum dolor sit amet, consectetur adipiscing elit</p>
<div class="btn" style="left:62px;top:2707px;width:138px;height:43px">KNOW MORE</div>

<div class="photo" role="img" aria-label="Video still of a finger touching a glowing fingerprint scanner on a digital interface" style="left:590px;top:2395px;width:537px;height:364px;background:radial-gradient(circle at 60% 50%,#6fe2ea 0%,#1f8c9b 22%,#0e3f52 55%,#081c28 100%)"></div>
<div class="abs" style="left:606px;top:2405px;width:514px;height:348px;border:1.5px solid var(--orange)"></div>
<div class="abs" style="left:836px;top:2550px;width:50px;height:50px;border-radius:50%;background:var(--white);display:flex;align-items:center;justify-content:center">
  <svg width="18" height="18" viewBox="0 0 18 18"><path d="M5 3l11 6-11 6z" fill="#ee7d22"/></svg>
</div>

<!-- resources -->
<div class="sec-title" style="top:2938px">FEATURED <em>RESOURCES</em></div>
<div class="bar" style="left:570px;top:3007px"></div>

<div class="arrow-btn" style="left:38px"><svg width="12" height="12" viewBox="0 0 12 12" fill="none" stroke="#9aa2ad" stroke-width="2"><path d="M8 2L4 6l4 4"/></svg></div>
<div class="arrow-btn" style="left:1116px;border-color:var(--navy)"><svg width="12" height="12" viewBox="0 0 12 12" fill="none" stroke="#1f3a5f" stroke-width="2"><path d="M4 2l4 4-4 4"/></svg></div>

<div class="res" style="left:118px">
  <div class="img" role="img" aria-label="Finger touching a glowing screen with floating code tags" style="background:radial-gradient(circle at 60% 55%,#5fd8e6 0%,#1b6a86 35%,#0d2233 80%)"></div>
  <h4>Lorem ipsum dolor sit amet</h4><div class="u"></div>
  <p>Lorem ipsum dolor sit amet, consectetur adipisci elit, sed eiusmod tempor Lorem ipsum dolor sit amet</p>
  <div class="corner"></div>
  <svg class="corner-arrow" width="20" height="12" viewBox="0 0 20 12" fill="none" stroke="#fff" stroke-width="1.6"><path d="M1 6h17M13 1l5 5-5 5"/></svg>
</div>
<div class="res" style="left:448px">
  <div class="img" role="img" aria-label="Laptop with code on a teal and orange glowing background" style="background:linear-gradient(120deg,#2ea3a0 0%,#3fb6a8 40%,#d9633e 75%,#f08a5a 100%)"></div>
  <h4>Lorem ipsum dolor sit amet</h4><div class="u"></div>
  <p>Lorem ipsum dolor sit amet, consectetur adipisci elit, sed eiusmod tempor Lorem ipsum dolor sit amet</p>
  <div class="corner"></div>
  <svg class="corner-arrow" width="20" height="12" viewBox="0 0 20 12" fill="none" stroke="#fff" stroke-width="1.6"><path d="M1 6h17M13 1l5 5-5 5"/></svg>
</div>
<div class="res" style="left:778px">
  <div class="img" role="img" aria-label="Hands typing on a laptop keyboard under blue light" style="background:linear-gradient(135deg,#5d7ea6 0%,#8ea8c7 45%,#d7e0ea 100%)"></div>
  <h4>Lorem ipsum dolor sit amet</h4><div class="u"></div>
  <p>Lorem ipsum dolor sit amet, consectetur adipisci elit, sed eiusmod tempor Lorem ipsum dolor sit amet</p>
  <div class="corner"></div>
  <svg class="corner-arrow" width="20" height="12" viewBox="0 0 20 12" fill="none" stroke="#fff" stroke-width="1.6"><path d="M1 6h17M13 1l5 5-5 5"/></svg>
</div>

<!-- partners -->
<div class="sec-title" style="top:3605px">CREATED BY US, <em>TRUSTED BY YOU.</em></div>
<div class="bar" style="left:570px;top:3688px"></div>

<div class="partner" style="left:88px;width:189px"><span class="dot"></span>Maldreth</div>
<div class="partner" style="left:294px;width:190px;font-size:16px"><span class="dot"></span>Ostrava Labs</div>
<div class="partner" style="left:506px;width:191px"><span class="dot"></span>Quorvel</div>
<div class="partner" style="left:712px;width:190px"><span class="dot"></span>Pellucia</div>
<div class="partner" style="left:922px;width:189px"><span class="dot"></span>Tenvari</div>

<!-- footer -->
<footer class="footer">
  <h5 style="left:305px;top:50px">QUICK LINKS</h5>
  <ul class="qlinks">
    <li>About Us</li><li>Solutions</li><li>Case Studies</li><li>Careers</li><li>Contact</li>
  </ul>
  <div class="abs brand" style="left:500px;top:95px;font-size:40px"><span class="mark" style="width:30px;height:30px;background:var(--white)"></span>BrimLoop</div>
  <h5 style="left:770px;top:45px">CONTACT US</h5>
  <div class="contact-row" style="top:100px"><span class="box"><svg width="12" height="12" viewBox="0 0 12 12" fill="none" stroke="#fff" stroke-width="1.3"><path d="M2 1h3l1 3-2 1a7 7 0 0 0 3 3l1-2 3 1v3c-6 0-9-3-9-9z"/></svg></span><span>CALL US<br>555 0148 2290</span></div>
  <div class="contact-row" style="top:150px"><span class="box"><svg width="12" height="10" viewBox="0 0 12 10" fill="none" stroke="#fff" stroke-width="1.3"><rect x="1" y="1" width="10" height="8"/><path d="M1 1l5 4 5-4"/></svg></span><span>EMAIL US<br>hello@brimloop-mail.com</span></div>
  <div class="contact-row" style="top:200px"><span class="box"><svg width="10" height="13" viewBox="0 0 10 13" fill="none" stroke="#fff" stroke-width="1.3"><path d="M5 12S1 7 1 5a4 4 0 0 1 8 0c0 2-4 7-4 7z"/><circle cx="5" cy="5" r="1.4"/></svg></span><span>Address line Dummy Here<br>Address line Here</span></div>
</footer>
<div class="social" style="left:566px"></div>
<div class="social" style="left:605px"></div>
<div class="copy">© 2025 BrimLoop. All Rights Reserved.</div>

</body>
</html>
```